Velvet Paw Hospital Business Card Design

I need a business card designed for my cat only veterinary clinic. I will upload the logo that I would like included on the card. Please include:
Business Name: The Velvet Paw Hospital
Address: 20947 E. 38th St, Scottsdale, AZ 85371
Phone #: 480-555-6143
Website URL: www.velvetpawvets.com
And the Doctors Name: Marisol Brenn, DVM

```html
<!DOCTYPE html>
<html lang="en">
<head>
<meta charset="utf-8">
<title>The Velvet Paw Hospital – Business Card</title>
<link rel="stylesheet" href="https://fonts.googleapis.com/css2?family=Montserrat:wght@400;600&family=Quicksand:wght@500&display=swap">
<style>
  :root {
    --page-bg: #3a3a3a;
    --card-white: #ffffff;
    --card-black: #141414;
    --accent-blue: #2b8cc4;
    --ink: #2b2b2b;
    --logo-night: #2a1a3a;
    --logo-violet: #6a3a9a;
    --logo-green: #3fb84a;
  }
  html, body {
    margin: 0;
    padding: 0;
    width: 1200px;
    height: 1200px;
    overflow: hidden;
    background: var(--page-bg);
  }
  .canvas {
    position: relative;
    width: 1200px;
    height: 1200px;
  }
  .card {
    position: absolute;
    left: 180px;
    width: 840px;
    height: 480px;
    border-radius: 36px;
    overflow: hidden;
    box-shadow: 0 18px 40px rgba(0,0,0,0.45);
  }
  .card--front { top: 70px; background: var(--card-white); }
  .card--back  { top: 650px; background: var(--card-black); }

  .logo-disc {
    position: absolute;
    border-radius: 50%;
    background: radial-gradient(circle at 50% 45%, var(--logo-green) 0%, var(--logo-violet) 45%, var(--logo-night) 75%);
  }
  .card--front .logo-disc { width: 230px; height: 230px; right: 100px; top: 70px; }
  .card--back .logo-disc  { width: 210px; height: 210px; left: 150px; top: 135px; }

  .identity {
    position: absolute;
    left: 80px;
    top: 215px;
    padding-left: 18px;
    border-left: 7px solid var(--accent-blue);
    font-family: "Montserrat", sans-serif;
  }
  .identity__name {
    margin: 0;
    font-size: 40px;
    font-weight: 600;
    line-height: 1;
    letter-spacing: 0.5px;
    color: var(--accent-blue);
    text-transform: uppercase;
    white-space: nowrap;
  }
  .identity__title {
    margin: 2px 0 0;
    font-size: 22px;
    font-weight: 400;
    color: var(--ink);
  }

  .contacts {
    position: absolute;
    left: 110px;
    top: 310px;
    margin: 0;
    padding: 0;
    list-style: none;
    font-family: "Montserrat", sans-serif;
    font-size: 23px;
    color: var(--ink);
  }
  .contacts__item {
    display: flex;
    align-items: center;
    gap: 16px;
    margin-bottom: 8px;
    line-height: 1.05;
    white-space: nowrap;
  }
  .contacts__icon {
    flex: none;
    width: 40px;
    height: 40px;
  }

  .brand-name {
    position: absolute;
    left: 395px;
    top: 178px;
    margin: 0;
    font-family: "Quicksand", sans-serif;
    font-weight: 500;
    font-size: 52px;
    line-height: 1.15;
    letter-spacing: 2px;
    color: #ffffff;
    white-space: nowrap;
  }
</style>
</head>
<body>
<main class="canvas">

  <section class="card card--front">
    <div class="logo-disc" role="img" aria-label="Clinic logo placeholder"></div>

    <div class="identity">
      <h1 class="identity__name">Marisol Brenn</h1>
      <p class="identity__title">DVM</p>
    </div>

    <ul class="contacts">
      <li class="contacts__item">
        <svg class="contacts__icon" viewBox="0 0 40 40" aria-hidden="true">
          <circle cx="20" cy="20" r="20" fill="var(--accent-blue)"/>
          <path d="M14 11c1.5-1 3 2 3.5 3.5.3 1-1 2-1.5 2.5 1 2.5 3 4.5 5.5 5.5.5-.5 1.5-1.8 2.5-1.5 1.5.5 4.5 2 3.5 3.5-1 1.5-2.5 3-5 2.5C16 26 13 23 11.5 17c-.5-2.5 1-4.5 2.5-6z" fill="#fff"/>
        </svg>
        <span>480-555-6143</span>
      </li>
      <li class="contacts__item">
        <svg class="contacts__icon" viewBox="0 0 40 40" aria-hidden="true">
          <circle cx="20" cy="20" r="20" fill="var(--accent-blue)"/>
          <g fill="none" stroke="#fff" stroke-width="1.8">
            <circle cx="20" cy="20" r="10"/>
            <ellipse cx="20" cy="20" rx="4.5" ry="10"/>
            <line x1="10" y1="20" x2="30" y2="20"/>
            <line x1="12" y1="15" x2="28" y2="15"/>
            <line x1="12" y1="25" x2="28" y2="25"/>
          </g>
        </svg>
        <span>www.velvetpawvets.com</span>
      </li>
      <li class="contacts__item">
        <svg class="contacts__icon" viewBox="0 0 40 40" aria-hidden="true">
          <circle cx="20" cy="20" r="20" fill="var(--accent-blue)"/>
          <path d="M20 9a7.5 7.5 0 0 0-7.5 7.5C12.5 22 20 31 20 31s7.5-9 7.5-14.5A7.5 7.5 0 0 0 20 9z" fill="#fff"/>
          <circle cx="20" cy="16.5" r="3" fill="var(--accent-blue)"/>
        </svg>
        <span>20947 E. 38th St,<br>Scottsdale, AZ 85371</span>
      </li>
    </ul>
  </section>

  <section class="card card--back">
    <div class="logo-disc" role="img" aria-label="Clinic logo placeholder"></div>
    <h2 class="brand-name">The Velvet Paw<br>Hospital</h2>
  </section>

</main>
</body>
</html>
```